Forward Thinking Civil Engineering Company Brochure

Objective: Create a visually compelling marketing folder that effectively communicates the company’s commitment to technical excellence, quality control, responsiveness, and sustainability. Design cascading card inserts for more details on each service area.

Use: The folder will be used for client meetings, proposals, and trade shows to present services, capabilities, and case studies in a structured and engaging manner. Front, back, and pockets may be used for design but one pocket should have location for business card.

Company Identity: Modern, innovative, and sustainability-focused.
Color Scheme/Typography: Align with our brand (see attached... the neutral color can be adjusted)
Style: Clean, professional, and forward-thinking perhaps with subtle technical elements (blueprints, grids, engineering icons).

Folder Size: Standard 9” x 12” presentation folder with pockets.
Branding Elements: Must include certifications (see www.q7veng.com homepage for the certifications...HUB, SBA etc)
Logo placement (front cover and inside pocket).

q7veng.com is old website do not pull branding concepts

Cascading Design: Insert cards should be stacked inside the folder, with visible section titles when inserted.
Left Pocket – 4 Cascading Cards (About Q7V, PS&E, Geotechnical Engineering, Construction Material Testing)
Largest: 8.75" x 11.5"
Medium-Large: 8.75" x 10.75"
Medium: 8.75" x 10"
Smallest: 8.75" x 9.25"
Right Pocket – 4 Cascading Cards (Construction, Engineering & Testing, Construction Management, Environmental Engineering, Drone and GIS Services)
Largest: 8.75" x 11.5"
Medium: 8.75" x 10"
Smallest: 8.75" x 9.25"

```html
<!DOCTYPE html>
<html lang="en">
<head>
<meta charset="utf-8">
<title>Q7V Engineering – Presentation Folder</title>
<link href="https://fonts.googleapis.com/css2?family=Montserrat:wght@400;600;700;800&family=Open+Sans:wght@400;600&display=swap" rel="stylesheet">
<style>
:root{
  --navy:#2b3a4f;
  --navy-deep:#1f2b3b;
  --orange:#d9621e;
  --orange-soft:#e98a4b;
  --stone:#ecebe8;
  --stone-dark:#d6d3ce;
  --ink:#3c4450;
  --white:#ffffff;
  --page:#f4f4f2;
}
*{box-sizing:border-box;margin:0;padding:0}
html,body{width:1200px;height:2316px;overflow:hidden;background:var(--page)}
body{position:relative;font-family:"Open Sans",Arial,sans-serif;color:var(--ink)}
.abs{position:absolute}
.photo{position:absolute}
.heading{font-family:"Montserrat",Arial,sans-serif}

/* logo lockup */
.brand{display:flex;align-items:center;gap:6px;font-family:"Montserrat",Arial,sans-serif;font-weight:800;color:var(--navy);letter-spacing:.5px;white-space:nowrap}
.brand .mark{width:14px;height:14px;background:var(--orange);flex:none}
.brand.light{color:var(--white)}

/* ---------- outside cover (1120 x 480) ---------- */
.cover{position:absolute;width:1120px;height:480px;overflow:hidden;box-shadow:0 6px 18px rgba(0,0,0,.18);background:var(--stone)}
.cover .back{position:absolute;left:0;top:0;width:560px;height:480px;background:var(--stone)}
.cover .back .photo{left:0;top:0;width:560px;height:250px;clip-path:polygon(0 0,100% 0,100% 70%,82% 100%,0 100%);background:linear-gradient(160deg,#b9b7b2,#6f6d69 70%,#8a8782)}
.cover .years{left:34px;top:270px;background:var(--orange);color:var(--white);font-weight:700;font-size:17px;padding:8px 16px;letter-spacing:1px}
.cover .back-brand{left:34px;top:322px;font-size:24px}
.cover .services{left:34px;top:360px;font-size:10px;letter-spacing:2px;font-weight:700;color:var(--navy)}
.cover .intro{left:34px;top:382px;width:420px;font-size:11px;line-height:1.5}
.cover .badges{left:34px;top:428px;display:flex;gap:10px}
.cover .badges span{width:44px;height:28px;background:var(--stone-dark);border-radius:3px}
.cover .front{position:absolute;left:560px;top:0;width:560px;height:480px;background:var(--white)}
.cover .front .bar{position:absolute;left:0;top:0;width:560px;height:64px;background:var(--white);border-bottom:4px solid var(--orange)}
.cover .front .bar .brand{position:absolute;left:28px;top:18px;font-size:24px}
.cover .front .bar .slant{position:absolute;right:0;top:0;width:170px;height:60px;background:var(--navy);clip-path:polygon(22% 0,100% 0,100% 100%,0 100%)}
.cover .front .p1{left:0;top:68px;width:290px;height:196px;background:linear-gradient(150deg,#d9c9a5,#8d8a7f 60%,#c9893f)}
.cover .front .p2{left:294px;top:68px;width:266px;height:196px;background:linear-gradient(170deg,#a9c3d8,#d7c6a4 55%,#a88b5c)}
.cover .front .panel{position:absolute;left:0;top:264px;width:560px;height:216px;background:var(--navy);clip-path:polygon(0 14%,100% 0,100% 100%,0 100%)}
.cover .front .stripe{position:absolute;left:0;top:256px;width:560px;height:12px;background:var(--orange);clip-path:polygon(0 100%,100% 0,100% 30%,0 100%)}
.cover .headline{left:90px;top:312px;color:var(--white);font-weight:800;font-size:30px;line-height:1.2;letter-spacing:1px}
.cover .headline li{list-style:none;display:flex;align-items:center;gap:14px}
.cover .headline li::before{content:"";width:12px;height:12px;background:var(--orange)}
.cover .place{left:116px;top:432px;color:var(--orange-soft);font-weight:700;font-size:13px;letter-spacing:3px}

/* ---------- inside spread ---------- */
.inside{position:absolute;left:40px;top:560px;width:1120px;height:660px;box-shadow:0 6px 18px rgba(0,0,0,.18);overflow:hidden}
.inside .panel{position:absolute;top:0;width:560px;height:660px;background:var(--stone);overflow:hidden}
.inside .panel.left{left:0}
.inside .panel.right{left:560px;border-left:1px solid var(--stone-dark)}
.inside .shape-navy{position:absolute;left:0;top:0;width:560px;height:230px;background:var(--navy);clip-path:polygon(0 0,100% 0,100% 55%,0 100%)}
.inside .shape-orange{position:absolute;left:0;top:180px;width:560px;height:90px;background:var(--orange);clip-path:polygon(0 55%,100% 0,100% 30%,0 100%)}
.inside .pocket{position:absolute;left:0;top:420px;width:560px;height:240px;background:var(--navy);clip-path:polygon(0 18%,100% 0,100% 100%,0 100%);z-index:3}
.inside .pocket-edge{position:absolute;left:0;top:412px;width:560px;height:52px;background:var(--orange);clip-path:polygon(0 100%,100% 0,100% 22%,0 100%);z-index:4}
.inside .pocket .brand{position:absolute;left:50%;top:120px;transform:translateX(-50%);font-size:30px}
.inside .bc-slot{position:absolute;left:340px;top:470px;width:170px;height:96px;border:2px dashed var(--orange-soft);z-index:5}
.inside .card-holder{position:absolute;left:62px;top:40px;width:272px;height:340px;transform:scale(1.6);transform-origin:0 0;z-index:2}

/* ---------- insert card (272 x 340) ---------- */
.card{position:absolute;width:272px;height:340px;background:var(--white);overflow:hidden;box-shadow:0 3px 8px rgba(0,0,0,.2)}
.card .head{position:absolute;left:0;top:0;width:272px;height:34px;background:var(--stone)}
.card .head .brand{position:absolute;left:10px;top:10px;font-size:11px;gap:4px}
.card .head .brand .mark{width:9px;height:9px}
.card .head .slant{position:absolute;right:0;top:0;width:120px;height:34px;background:var(--navy);clip-path:polygon(18% 0,100% 0,100% 100%,0 100%)}
.card .head .slant::after{content:"";position:absolute;left:0;bottom:0;width:100%;height:4px;background:var(--orange)}
.card .photo{left:0;top:34px;width:272px;height:138px;clip-path:polygon(0 0,100% 0,100% 82%,70% 100%,0 100%)}
.card .title{position:absolute;left:0;top:176px;width:272px;padding:6px 12px 6px 16px;border-left:5px solid var(--orange)}
.card .title small{display:block;font-family:"Montserrat",Arial,sans-serif;font-weight:700;font-size:8px;letter-spacing:2px;color:var(--orange)}
.card .title h3{font-family:"Montserrat",Arial,sans-serif;font-weight:800;font-size:14px;line-height:1.15;color:var(--navy);text-transform:uppercase}
.card .body{position:absolute;left:16px;top:240px;width:140px;font-size:7.5px;line-height:1.5}
.card .ticks{position:absolute;left:166px;top:240px;width:96px;list-style:none}
.card .ticks li{display:flex;align-items:center;gap:5px;font-size:7.5px;font-weight:600;color:var(--navy);margin-bottom:7px}
.card .ticks li::before{content:"";width:8px;height:8px;background:var(--orange);flex:none}
.card .foot{position:absolute;left:0;bottom:0;width:272px;height:28px;background:var(--navy);color:var(--white);font-size:8px;font-weight:600;padding:9px 14px;letter-spacing:.5px}
.card .foot::before{content:"";position:absolute;right:0;top:0;width:70px;height:28px;background:var(--orange);clip-path:polygon(30% 0,100% 0,100% 100%,0 100%)}

/* ---------- small pieces ---------- */
.mini-cover{position:absolute;left:600px;top:1270px;width:1120px;height:480px;transform:scale(.5);transform-origin:0 0}
.bizcard{position:absolute;width:240px;height:130px;box-shadow:0 3px 8px rgba(0,0,0,.18);overflow:hidden}
.bizcard.front{left:60px;top:1340px;background:var(--white)}
.bizcard.front .brand{position:absolute;left:18px;top:52px;font-size:15px;gap:5px}
.bizcard.front .brand .mark{width:11px;height:11px}
.bizcard.front .band{position:absolute;left:0;bottom:0;width:240px;height:16px;background:var(--orange)}
.bizcard.back{left:316px;top:1340px;background:var(--navy);color:var(--white)}
.bizcard.back .who{position:absolute;left:16px;top:16px;font-family:"Montserrat",Arial,sans-serif;font-weight:700;font-size:12px}
.bizcard.back .role{position:absolute;left:16px;top:33px;font-size:8px;color:var(--orange-soft);letter-spacing:1px}
.bizcard.back .lines{position:absolute;left:16px;top:62px;font-size:8px;line-height:1.6}
.bizcard.back .wedge{position:absolute;right:0;top:0;width:70px;height:130px;background:var(--orange);clip-path:polygon(50% 0,100% 0,100% 100%,0 100%)}
</style>
</head>
<body>

<!-- Outside cover spread -->
<section class="cover" style="left:40px;top:40px" aria-label="Folder outside spread">
  <div class="back">
    <div class="photo" role="img" aria-label="Photo of a road roller compacting asphalt"></div>
    <div class="abs years heading">15 YEARS OF EXPERIENCE</div>
    <div class="abs brand back-brand"><span class="mark"></span>Q7V ENGINEERING</div>
    <div class="abs services heading">SURVEY · DESIGN · TESTING · INSPECTION</div>
    <p class="abs intro">Serving public and private clients across the Rio Grande Valley with responsive engineering.</p>
    <div class="abs badges"><span></span><span></span><span></span><span></span><span></span></div>
  </div>
  <div class="front">
    <div class="bar"><div class="brand"><span class="mark"></span>Q7V ENGINEERING</div><div class="slant"></div></div>
    <div class="photo p1" role="img" aria-label="Photo of engineers in hard hats reviewing plans on site"></div>
    <div class="photo p2" role="img" aria-label="Photo of a highway overpass under construction"></div>
    <div class="stripe"></div>
    <div class="panel"></div>
    <ul class="abs headline heading"><li>PLANNING</li><li>DESIGN</li><li>CONSTRUCTION</li></ul>
    <div class="abs place heading">IN MISSION TX</div>
  </div>
</section>

<!-- Inside spread with pockets -->
<section class="inside" aria-label="Folder inside spread">
  <div class="panel left">
    <div class="shape-navy"></div><div class="shape-orange"></div>
    <div class="card-holder">
      <article class="card">
        <div class="head"><div class="brand"><span class="mark"></span>Q7V ENGINEERING</div><div class="slant"></div></div>
        <div class="photo" role="img" aria-label="Photo of road rollers paving a highway" style="background:linear-gradient(160deg,#c7b9a0,#6b655c 60%,#d57a34)"></div>
        <div class="title"><small>ABOUT</small><h3>PS&amp;E</h3></div>
      </article>
    </div>
    <div class="pocket-edge"></div>
    <div class="pocket"><div class="brand light"><span class="mark"></span>Q7V ENGINEERING</div></div>
  </div>
  <div class="panel right">
    <div class="shape-navy"></div><div class="shape-orange"></div>
    <div class="card-holder">
      <article class="card">
        <div class="head"><div class="brand"><span class="mark"></span>Q7V ENGINEERING</div><div class="slant"></div></div>
        <div class="photo" role="img" aria-label="Photo of a survey drone flying over a site" style="background:linear-gradient(170deg,#b8cde0,#8fa7bd 60%,#a0927c)"></div>
        <div class="title"><small>ABOUT</small><h3>Drone and GIS Services</h3></div>
      </article>
    </div>
    <div class="pocket-edge"></div>
    <div class="pocket"></div>
    <div class="bc-slot" aria-label="Business card slot"></div>
  </div>
</section>

<!-- Business cards -->
<div class="bizcard front"><div class="brand"><span class="mark"></span>Q7V ENGINEERING</div><div class="band"></div></div>
<div class="bizcard back">
  <div class="who">Daniel Ortiz, P.E.</div>
  <div class="role">PROJECT MANAGER</div>
  <div class="lines">(956) 555-0142<br>info@q7veng.com<br>www.q7veng.com</div>
  <div class="wedge"></div>
</div>

<!-- Outside spread, flat, small -->
<section class="cover mini-cover" aria-label="Folder outside spread, reduced">
  <div class="back">
    <div class="photo" role="img" aria-label="Photo of a road roller compacting asphalt"></div>
    <div class="abs years heading">15 YEARS OF EXPERIENCE</div>
    <div class="abs brand back-brand"><span class="mark"></span>Q7V ENGINEERING</div>
    <div class="abs services heading">SURVEY · DESIGN · TESTING · INSPECTION</div>
    <p class="abs intro">Serving public and private clients across the Rio Grande Valley with responsive engineering.</p>
    <div class="abs badges"><span></span><span></span><span></span><span></span><span></span></div>
  </div>
  <div class="front">
    <div class="bar"><div class="brand"><span class="mark"></span>Q7V ENGINEERING</div><div class="slant"></div></div>
    <div class="photo p1" role="img" aria-label="Photo of engineers in hard hats reviewing plans on site"></div>
    <div class="photo p2" role="img" aria-label="Photo of a highway overpass under construction"></div>
    <div class="stripe"></div>
    <div class="panel"></div>
    <ul class="abs headline heading"><li>PLANNING</li><li>DESIGN</li><li>CONSTRUCTION</li></ul>
    <div class="abs place heading">IN MISSION TX</div>
  </div>
</section>

<!-- Insert cards -->
<section class="card-grid" aria-label="Insert cards">
  <article class="card" style="left:32px;top:1560px">
    <div class="head"><div class="brand"><span class="mark"></span>Q7V ENGINEERING</div><div class="slant"></div></div>
    <div class="photo" role="img" aria-label="Photo of a technician drilling soil samples" style="background:linear-gradient(160deg,#c9b79a,#7a6a55 60%,#d8792f)"></div>
    <div class="title"><small>ABOUT</small><h3>Geotechnical Engineering</h3></div>
    <p class="body">Field-proven teams deliver reliable results on every project, on schedule and within budget.</p>
    <ul class="ticks"><li>Soil borings</li><li>Foundation design</li><li>Slope stability</li></ul>
    <div class="foot">www.q7veng.com</div>
  </article>
  <article class="card" style="left:320px;top:1560px">
    <div class="head"><div class="brand"><span class="mark"></span>Q7V ENGINEERING</div><div class="slant"></div></div>
    <div class="photo" role="img" aria-label="Photo of a concrete building under construction" style="background:linear-gradient(160deg,#aebdcc,#6d747c 60%,#b8aa92)"></div>
    <div class="title"><small>ABOUT</small><h3>Construction Material Testing</h3></div>
    <p class="body">Field-proven teams deliver reliable results on every project, on schedule and within budget.</p>
    <ul class="ticks"><li>Concrete testing</li><li>Asphalt testing</li><li>Lab services</li></ul>
    <div class="foot">www.q7veng.com</div>
  </article>
  <article class="card" style="left:608px;top:1560px">
    <div class="head"><div class="brand"><span class="mark"></span>Q7V ENGINEERING</div><div class="slant"></div></div>
    <div class="photo" role="img" aria-label="Photo of a highway interchange" style="background:linear-gradient(170deg,#b4c8da,#cdbb9a 55%,#8f7a5a)"></div>
    <div class="title"><small>ABOUT</small><h3>Q7V</h3></div>
    <p class="body">Field-proven teams deliver reliable results on every project, on schedule and within budget.</p>
    <ul class="ticks"><li>Quality control</li><li>Responsiveness</li><li>Sustainability</li></ul>
    <div class="foot">www.q7veng.com</div>
  </article>
  <article class="card" style="left:896px;top:1560px">
    <div class="head"><div class="brand"><span class="mark"></span>Q7V ENGINEERING</div><div class="slant"></div></div>
    <div class="photo" role="img" aria-label="Photo of road rollers paving a highway" style="background:linear-gradient(160deg,#c7b9a0,#6b655c 60%,#d57a34)"></div>
    <div class="title"><small>ABOUT</small><h3>PS&amp;E</h3></div>
    <p class="body">Field-proven teams deliver reliable results on every project, on schedule and within budget.</p>
    <ul class="ticks"><li>Plans</li><li>Specifications</li><li>Estimates</li></ul>
    <div class="foot">www.q7veng.com</div>
  </article>

  <article class="card" style="left:32px;top:1920px">
    <div class="head"><div class="brand"><span class="mark"></span>Q7V ENGINEERING</div><div class="slant"></div></div>
    <div class="photo" role="img" aria-label="Photo of a lab technician testing material samples" style="background:linear-gradient(160deg,#d8b48a,#8a6a4a 60%,#c9702c)"></div>
    <div class="title"><small>ABOUT</small><h3>Construction, Engineering &amp; Testing</h3></div>
    <p class="body">Field-proven teams deliver reliable results on every project, on schedule and within budget.</p>
    <ul class="ticks"><li>Inspection</li><li>Engineering</li><li>Testing</li></ul>
    <div class="foot">www.q7veng.com</div>
  </article>
  <article class="card" style="left:320px;top:1920px">
    <div class="head"><div class="brand"><span class="mark"></span>Q7V ENGINEERING</div><div class="slant"></div></div>
    <div class="photo" role="img" aria-label="Photo of a construction crew on a building site" style="background:linear-gradient(160deg,#c9c2b4,#7c7468 60%,#c98a4a)"></div>
    <div class="title"><small>ABOUT</small><h3>Construction Management</h3></div>
    <p class="body">Field-proven teams deliver reliable results on every project, on schedule and within budget.</p>
    <ul class="ticks"><li>Scheduling</li><li>Cost control</li><li>Site oversight</li></ul>
    <div class="foot">www.q7veng.com</div>
  </article>
  <article class="card" style="left:608px;top:1920px">
    <div class="head"><div class="brand"><span class="mark"></span>Q7V ENGINEERING</div><div class="slant"></div></div>
    <div class="photo" role="img" aria-label="Photo of an environmental field assessment" style="background:linear-gradient(160deg,#d9a46a,#9a6a3f 60%,#e0893c)"></div>
    <div class="title"><small>ABOUT</small><h3>Environmental Engineering</h3></div>
    <p class="body">Field-proven teams deliver reliable results on every project, on schedule and within budget.</p>
    <ul class="ticks"><li>Site assessment</li><li>Permitting</li><li>Compliance</li></ul>
    <div class="foot">www.q7veng.com</div>
  </article>
  <article class="card" style="left:896px;top:1920px">
    <div class="head"><div class="brand"><span class="mark"></span>Q7V ENGINEERING</div><div class="slant"></div></div>
    <div class="photo" role="img" aria-label="Photo of a survey drone flying over a site" style="background:linear-gradient(170deg,#b8cde0,#8fa7bd 60%,#a0927c)"></div>
    <div class="title"><small>ABOUT</small><h3>Drone and GIS Services</h3></div>
    <p class="body">Field-proven teams deliver reliable results on every project, on schedule and within budget.</p>
    <ul class="ticks"><li>Aerial mapping</li><li>GIS data</li><li>Site imaging</li></ul>
    <div class="foot">www.q7veng.com</div>
  </article>
</section>

</body>
</html>
```